Layout für Broschüre für chemiefreie Lösung, Kühlwasser aufzubereiten
Zielgruppe
VELTROMAX hat eine Technologie entwickelt, die in der Industrie eingesetzt wird um in geschlossenen und offenen Kühlkreisläufen ohne Biozide und Korrosion Inhibitoren das Kühlwasser aufzubereiten. Mit VELTROMAX haben die Unternehmen eine chemiefreie Lösungen gegen Biofouling, Korrosion und Kalk. Zielgruppe sind alle Unternehmen die etwas produzieren oder Klimaanlagen / Heizungssysteme betreiben. Es geht um zukunftsorientierte und vor allem nachhaltige Technologie ohne Einsatz von Chemie.
Aufgabenstellung
Wir suchen für die Broschüre ein neues Layout, dass geradlinig und klar strukturiert ist, vor allem modern. Die Broschüre sollte DIN A 4 - Format sein in der gewohnten Struktur Umschlagseite innen und außen und 8 - 10 Innenseiten. Im Layout sollte ein roter Faden zu erkennen sein, aber nicht jede Seite gleich aussehen. Die Anlagen sind nur beispielhaft vom bestehenden Material und sollten vom Layout keinesfalls eine Orientierung geben, denn das soll verändert werden. Die Anlagen sind für einen inhaltlichen Überblick.

```html
<!DOCTYPE html>
<html lang="de">
<head>
<meta charset="utf-8">
<title>VELTROMAX – Wirkungsweise</title>
<link href="https://fonts.googleapis.com/css2?family=Montserrat:wght@400;500;600;700&display=swap" rel="stylesheet">
<style>
  :root {
    --backdrop: #dcdcdd;
    --paper: #f7f7f8;
    --navy: #24244d;
    --navy-deep: #1a1a38;
    --teal: #4fb4cb;
    --frame: #2e2e58;
    --ink: #4a4a55;
    --circle: #a0a3a8;
    --muted: #6f7190;
    --photo-dark: #0d0d0e;
    --photo-mid: #2a2524;
  }
  * { box-sizing: border-box; margin: 0; padding: 0; }
  html, body {
    width: 1200px; height: 900px; overflow: hidden;
    background: var(--backdrop);
    font-family: "Montserrat", sans-serif;
  }
  .spread {
    position: absolute; left: 63px; top: 70px;
    width: 1074px; height: 760px;
    display: flex;
    box-shadow: 0 14px 40px rgba(0,0,0,.18);
  }
  .page { position: relative; width: 537px; height: 760px; }
  .page--left { background: var(--paper); }

  .section-title {
    position: absolute; left: 50%; top: 150px; transform: translateX(-50%);
    width: 320px; height: 64px;
    border: 2px solid var(--frame);
    display: flex; align-items: center; justify-content: center;
    color: var(--teal); font-weight: 600; font-size: 22px; letter-spacing: 3px;
  }
  .intro {
    position: absolute; left: 60px; right: 60px; top: 252px;
    text-align: center; color: var(--ink);
    font-size: 12.5px; font-weight: 500; letter-spacing: 1.6px; line-height: 1.55;
    text-transform: uppercase;
  }
  .steps-band {
    position: absolute; left: 0; right: 0; top: 320px; height: 330px;
    background: linear-gradient(180deg, var(--navy) 0%, var(--navy-deep) 100%);
    display: flex; justify-content: center; gap: 34px; padding-top: 60px;
  }
  .step { width: 130px; text-align: center; }
  .step__dot {
    width: 78px; height: 78px; border-radius: 50%;
    background: var(--circle); margin: 0 auto 26px;
  }
  .step__label { color: var(--teal); font-size: 12px; font-weight: 700; letter-spacing: 1.5px; }
  .step__subtitle {
    color: var(--muted); font-size: 8.5px; letter-spacing: 1px; margin-top: 4px;
    text-transform: uppercase;
  }
  .step__text { color: var(--muted); font-size: 7.5px; line-height: 1.5; margin-top: 10px; opacity: .8; }

  .folio {
    position: absolute; left: 24px; bottom: 22px;
    font-size: 7px; color: var(--ink); letter-spacing: .5px;
  }

  .page--right { overflow: hidden; }
  .hero-photo {
    width: 100%; height: 100%;
    background: radial-gradient(ellipse at 55% 55%, var(--photo-mid) 0%, var(--photo-dark) 65%);
  }
</style>
</head>
<body>
  <main class="spread">
    <section class="page page--left">
      <h1 class="section-title">WIRKUNGSWEISE</h1>
      <p class="intro">Gent pediscitate peliquo destiam, quissus aut atury qui aut officil maximaion eum ullupta turi.</p>

      <div class="steps-band">
        <article class="step">
          <div class="step__dot"></div>
          <h2 class="step__label">SCHRITT 1</h2>
          <p class="step__subtitle">Inis enturit dolupta</p>
          <p class="step__text">Wasser fließt durch das Modul und wird ohne Zusatz von Chemie behandelt.</p>
        </article>
        <article class="step">
          <div class="step__dot"></div>
          <h2 class="step__label">SCHRITT 2</h2>
          <p class="step__subtitle">Explique core niendi</p>
          <p class="step__text">Ionen werden gezielt gelöst und binden Kalk im Kreislauf.</p>
        </article>
        <article class="step">
          <div class="step__dot"></div>
          <h2 class="step__label">SCHRITT 3</h2>
          <p class="step__subtitle">Di, bittaborrum q.</p>
          <p class="step__text">Alle Oberflächen bleiben frei von Biofilm, Korrosion und Ablagerungen im Betrieb.</p>
        </article>
      </div>

      <p class="folio">4 VELTROMAX</p>
    </section>

    <section class="page page--right">
      <div class="hero-photo" role="img" aria-label="Foto: Hände unter einem klaren Wasserstrahl vor dunklem Hintergrund"></div>
    </section>
  </main>
</body>
</html>
```